Solar appointment reminder card

We are looking for a new design for our appointment reminder card since we have changed our logo. The card should have the new logo along with space for the employee to hand write the customers appointment date, time, the employees name and phone number.
I've uploaded what our old basic appointment card looked like and our new logo.

The cards should be in a standard business card size and could be horizontal or vertical.

```html
<!DOCTYPE html>
<html lang="en">
<head>
<meta charset="utf-8">
<title>Appointment Reminder Card</title>
<link rel="stylesheet" href="https://fonts.googleapis.com/css2?family=Arimo:wght@400;700&display=swap">
<style>
  :root {
    --backdrop-light: #6b6b6b;
    --backdrop-dark: #3a3a3a;
    --sky-top: #1f5496;
    --sky-mid: #1a3f70;
    --panel-dark: #16233a;
    --accent-orange: #f7941d;
    --field-white: #ffffff;
    --label-grey: #444444;
  }
  html, body {
    margin: 0;
    padding: 0;
    width: 1200px;
    height: 900px;
    overflow: hidden;
  }
  body {
    background: radial-gradient(circle at 50% 35%, var(--backdrop-light), var(--backdrop-dark));
    font-family: "Arimo", Arial, sans-serif;
    position: relative;
  }
  .reminder-card {
    position: absolute;
    left: 75px;
    top: 150px;
    width: 1050px;
    height: 600px;
    overflow: hidden;
    box-shadow: 0 18px 40px rgba(0,0,0,0.45);
  }
  .card-photo {
    position: absolute;
    inset: 0;
    background: linear-gradient(175deg, var(--sky-top) 0%, var(--sky-mid) 35%, #243a5c 60%, var(--panel-dark) 100%);
  }
  .card-title {
    position: absolute;
    left: 70px;
    top: 100px;
    margin: 0;
    font-size: 31px;
    font-weight: 700;
    color: var(--accent-orange);
    letter-spacing: 0.5px;
  }
  .title-rule {
    position: absolute;
    left: 70px;
    top: 148px;
    width: 390px;
    height: 3px;
    background: var(--accent-orange);
  }
  .brand {
    position: absolute;
    right: 70px;
    top: 46px;
    display: flex;
    align-items: center;
    gap: 12px;
  }
  .brand-dot {
    width: 34px;
    height: 34px;
    border-radius: 50%;
    background: var(--accent-orange);
  }
  .brand-name {
    font-size: 30px;
    font-weight: 700;
    color: var(--accent-orange);
    letter-spacing: 1px;
  }
  .field {
    position: absolute;
    height: 48px;
    background: var(--field-white);
    display: flex;
    align-items: center;
    padding-left: 22px;
    box-sizing: border-box;
    font-size: 22px;
    color: var(--label-grey);
  }
  .field-blank-1 { left: 500px; right: 70px; top: 108px; }
  .field-blank-2 { left: 500px; right: 70px; top: 176px; }
  .field-for     { left: 70px; width: 410px; top: 244px; }
  .field-time    { left: 500px; right: 70px; top: 244px; }
  .field-date    { left: 70px; right: 70px; top: 312px; }
  .field-rep     { left: 70px; right: 70px; top: 380px; }
  .field-phone   { left: 70px; right: 70px; top: 448px; }
</style>
</head>
<body>
  <section class="reminder-card">
    <div class="card-photo" role="img" aria-label="Photo of rows of solar panels under a blue sky"></div>
    <h1 class="card-title">APPOINTMENT REMINDER</h1>
    <div class="title-rule"></div>
    <div class="brand">
      <span class="brand-dot"></span>
      <span class="brand-name">HELIO RIDGE SOLAR</span>
    </div>
    <div class="field field-blank-1"></div>
    <div class="field field-blank-2"></div>
    <div class="field field-for">For:</div>
    <div class="field field-time">Time :</div>
    <div class="field field-date">Date :</div>
    <div class="field field-rep">Representative :</div>
    <div class="field field-phone">Phone :</div>
  </section>
</body>
</html>
```